Serenity Prayer Art/Poster Design for Canvas Printing

I have been tasked with creating a piece of art containing the complete serenity prayer for a rehab in New York. The final design will essentially be split into 3 sections and printed on 3 canvases which will hang together (please see below for detailed final product requirements).

We are looking for something that has a classic feel to it, but itsn't overly flourish-y or cheezy as many "church-y" things can feel. Fonts similar to that used in the uploaded file are probably the safest but we don't want to inhibit what you would come up with creatively on your own. I am looking for some sort of background behind the words. This can be a picture, ambiance (sort of like in the attached file). It should be beautiful, refreshing and stunning to look at.

Please feel free to use any Lantern Fellowship symbols or colors (feel free to google, "The Lantern Fellowship Flag" "The Lantern Fellowship Crest" "The Lantern Fellowship Shield") in an abstract way in the background. I would not be looking for any literal or exact Fellowship symbols to appear, but using shadows, outlines, etc. is completely acceptable. I'm attaching some CD art which uses The Lantern Fellowship shield in the way I am describing. The words "The Lantern Fellowship" are removed and it is the outline of the shield used in a very modern, simplistic way. Red, Yellow and Blue would be the colors to use ideally as these are the colors of The Lantern Fellowship... you could even get creative and use a different color on each panel.

In the file you will find the complete Serenity prayer. The only words we want on the artwork is:

"God grant me the serenity to accept the things I cannot change; courage to change the things I can; and wisdom to know the difference. Living one day at a time; Enjoying one moment at a time; Accepting hardships as the pathway to peace; Taking, as He did, this sinful world as it is, not as I would have it; Trusting that He will make all things right if I surrender to His Will; That I may be reasonably happy in this life and supremely happy with Him forever in the next. Amen.

- Osmund Tavelli
Commissioned by Majors Dennis & Carla Vostrin"

Please do not italicize the font as it is in the reference.

We are printing the 3 sections on canvases sized 24"w x 48"h. Since there is a folded border that is 1.5" deep, the total size of the artwork should be 75"w x 51"h and we would be expecting 3 files each measuring 27"w x 51"h (to allow room for the border of each canvas while maintaining the integrity of the image as a whole). If there is any confusion as to what we are looking for in terms of dimensions or images, please let me know. It's much simpler than it seems.

I am attaching a VERY rough doodle of the layout to help with any questions.

We want something that is beautiful and inspiring and can't wait to see what you work on!

Target Market(s)

Will be used as hanging art in a rehab center.

Industry/Entity Type

Printing

Font styles to use
Other font styles liked:
• Can be a nice, modern Script font or somethings like Sans Serif.

Colors
0555a3
ec1f27
fbed22
85acd3
f59296
fbf289

Requirements
Must have
• The Serenity Prayer as noted in the notes.
Nice to have
• Modern, abstract use of a Lantern Fellowship symbol in the background somehow.

```html
<!DOCTYPE html>
<html lang="en">
<head>
<meta charset="utf-8">
<title>Serenity Prayer</title>
<link rel="stylesheet" href="https://fonts.googleapis.com/css2?family=Lobster&family=Libre+Baskerville:wght@400;700&display=swap">
<style>
  :root {
    --page-bg: #ffffff;
    --teal-deep: #1f6f78;
    --teal-soft: #5fa8a0;
    --sky-blue: #3f7fa6;
    --ember-red: #c9402a;
    --sunset-orange: #e8873a;
    --horizon-gold: #d9b25a;
    --title-yellow: #f6ec2a;
    --body-white: #ffffff;
    --text-shadow: rgba(20, 12, 8, 0.85);
  }
  * { margin: 0; padding: 0; box-sizing: border-box; }
  html, body {
    width: 1200px;
    height: 900px;
    overflow: hidden;
    background: var(--page-bg);
  }
  .triptych {
    position: absolute;
    left: 0;
    top: 42px;
    width: 1200px;
    height: 816px;
    overflow: hidden;
  }
  .triptych__backdrop {
    position: absolute;
    inset: 0;
    background:
      radial-gradient(ellipse 30% 28% at 90% 84%, rgba(30, 18, 12, 0.9), transparent 70%),
      radial-gradient(ellipse 45% 30% at 72% 12%, var(--ember-red), transparent 70%),
      radial-gradient(ellipse 40% 30% at 95% 40%, var(--sunset-orange), transparent 70%),
      radial-gradient(ellipse 35% 30% at 10% 12%, var(--sky-blue), transparent 70%),
      radial-gradient(ellipse 45% 35% at 15% 80%, var(--teal-soft), transparent 75%),
      linear-gradient(180deg,
        var(--teal-deep) 0%,
        var(--sunset-orange) 28%,
        var(--horizon-gold) 42%,
        #b79a5e 55%,
        var(--teal-soft) 72%,
        var(--teal-deep) 100%);
  }
  .triptych__seam {
    position: absolute;
    top: 0;
    bottom: 0;
    width: 6px;
    background: var(--page-bg);
  }
  .triptych__seam--left { left: 429px; }
  .triptych__seam--right { left: 765px; }
  .triptych__content {
    position: relative;
    z-index: 1;
    text-align: center;
    padding-top: 34px;
  }
  .triptych__title {
    font-family: "Lobster", cursive;
    font-weight: 400;
    font-size: 112px;
    line-height: 1.1;
    color: var(--title-yellow);
    text-shadow: 3px 4px 6px var(--text-shadow);
  }
  .prayer {
    margin-top: 16px;
    font-family: "Libre Baskerville", Georgia, serif;
    font-weight: 700;
    font-size: 28px;
    line-height: 1.4;
    color: var(--body-white);
    text-shadow: 2px 2px 4px var(--text-shadow);
  }
  .prayer__line { display: block; }
  .prayer__attribution {
    margin-top: 20px;
    margin-left: 220px;
    font-family: "Libre Baskerville", Georgia, serif;
    font-weight: 700;
    font-size: 23px;
    color: var(--body-white);
    text-shadow: 2px 2px 4px var(--text-shadow);
  }
  .prayer__commission {
    margin-top: 10px;
    margin-left: 220px;
    font-family: "Libre Baskerville", Georgia, serif;
    font-weight: 400;
    font-size: 18px;
    color: var(--body-white);
    text-shadow: 2px 2px 4px var(--text-shadow);
  }
</style>
</head>
<body>
  <main class="triptych">
    <div class="triptych__backdrop" role="img" aria-label="Textured sunset collage over water in teal, gold and red tones, with faint hymn lettering and a silhouette of a kneeling figure in prayer at lower right"></div>
    <div class="triptych__seam triptych__seam--left"></div>
    <div class="triptych__seam triptych__seam--right"></div>
    <div class="triptych__content">
      <h1 class="triptych__title">Serenity Prayer</h1>
      <p class="prayer">
        <span class="prayer__line">God grant me the serenity to accept the things I cannot change;</span>
        <span class="prayer__line">courage to change the things I can; and wisdom to know</span>
        <span class="prayer__line">the difference. Living one day at a time; Enjoying one moment</span>
        <span class="prayer__line">at a time; Accepting hardships as the pathway to peace;</span>
        <span class="prayer__line">Taking, as He did, this sinful world as it is, not as I would have it;</span>
        <span class="prayer__line">Trusting that He will make all things right if I surrender</span>
        <span class="prayer__line">to His Will; That I may be reasonably happy in this life</span>
        <span class="prayer__line">and supremely happy with Him Forever in the next.</span>
        <span class="prayer__line">Amen.</span>
      </p>
      <p class="prayer__attribution">-Osmund Tavelli</p>
      <p class="prayer__commission">Commissioned by Majors Dennis &amp; Carla Vostrin</p>
    </div>
  </main>
</body>
</html>
```